Wordpress Design and Coding for New Residential and Commercial Lawn and Landscape Co.

I need a Wordpress site with coding built for a startup Residential and Commercial Lawn and Landscape Company. I'm uploading our business card and logo files. I'd like a really clean design, with icons to describe services and who we serve. We don't have a lot of content being new.
We offer a large variety of services. Our 2 target customers would be residential and commercial. We offer the following services: Lawn Care and Mowing, Hedge and Shrub Trimming, Removal and Clean Up, Aeration and Sod, Mulch and Rock Installation, Landscape Installations and Renovations, and Commercial Snow Removal in the winter for Retail Shopping Centers, Communities, and other larger customers.
We serve Elmview County, Ridgefield County, and Surrounding areas.
Target Market(s)
We have 2 main types of customer.
1. Residential - this includes lawn maintenance, plantings, mulch & rock installs, and maintenance, etc.
2. Commercial - this includes complete care from design, planting, maintenance, etc. Communities, Property Managers, Housing Associations, Shopping Centers, Retail, etc.
Industry/Entity Type
Landscape
Coding
Coded - Design and coding required
Requirements
Must have
- Clean design. Nice distinct icons to display services and other information. Large Bold eye popping landscape photo at top.
- I've included screen shots of designs I like. Please do not copy them, they are competitors.
Nice to have
- 1. Link to our Facebook page - social.example.com/brightfurrowmd
- 2. Link to FB Photos for Gallery Section - https://www.example-social.com/pg/BrightFurrowMD/photos/
- 3. Why Choose Us section.
- 4. Contact form that includes 4 sections - Name, Phone #, Service Address, and Comments.
- 5. Reviews/Testimonials on Landing Page

```html
<!DOCTYPE html>
<html lang="en">
<head>
<meta charset="utf-8">
<title>Bright Furrow Lawn &amp; Landscape</title>
<link rel="stylesheet" href="https://fonts.googleapis.com/css2?family=Roboto:wght@300;400;500;700&family=PT+Serif:wght@400;700&display=swap">
<style>
:root{
  --green:#5ccd63;
  --green-dark:#3fae47;
  --ink:#2b2b2b;
  --text:#6b6b6b;
  --muted:#9a9a9a;
  --line:#e3e3e3;
  --dark:#3c3c3c;
  --darker:#2d2d2d;
  --light:#f3f3f3;
  --white:#ffffff;
}
*{box-sizing:border-box;margin:0;padding:0}
html,body{width:1200px;height:4337px;overflow:hidden}
body{font-family:"Roboto",Arial,sans-serif;color:var(--text);background:var(--white);position:relative}
.abs{position:absolute}
section,header,footer{position:absolute;left:0;width:1200px}
a{color:inherit;text-decoration:none}
.green{color:var(--green)}
.photo{position:absolute;display:block}
.btn{position:absolute;display:flex;align-items:center;justify-content:center;font-size:12px;font-weight:700;letter-spacing:.5px;text-transform:uppercase;color:var(--white);background:var(--green)}
.read-more{position:absolute;font-size:11px;font-weight:700;color:var(--green);text-transform:uppercase}
.section-title{position:absolute;font-size:28px;font-weight:700;color:var(--ink)}
.section-title .green{color:var(--green)}
.underline{position:absolute;height:2px;background:var(--line)}
.underline::before{content:"";position:absolute;left:0;top:0;width:60px;height:2px;background:var(--green)}

/* top bar */
.topbar{top:0;height:35px;background:rgba(40,40,40,.85);z-index:3;font-size:11px;color:#cfcfcf}
.topbar .tagline{left:101px;top:11px}
.topbar .info{left:600px;top:11px;display:flex;gap:18px;white-space:nowrap}
.topbar .socials{left:1030px;top:8px;display:flex;gap:8px}
.circle{display:block;width:19px;height:19px;border-radius:50%;border:1px solid #bdbdbd}

/* hero */
.hero{top:0;height:515px;background:linear-gradient(135deg,#8fa777 0%,#5f7d41 35%,#3d5a2a 70%,#6d8a53 100%)}
.hero .photo{inset:0}
.brand-box{left:93px;top:35px;width:341px;height:104px;background:var(--white);display:flex;align-items:center;justify-content:center;gap:12px;z-index:2}
.brand-dot{width:26px;height:26px;border-radius:50%;background:var(--green)}
.brand-name{font-size:26px;font-weight:700;color:var(--green-dark)}
.nav{left:420px;top:52px;width:679px;height:69px;background:var(--green);clip-path:polygon(40px 0,100% 0,100% 100%,0 100%);display:flex;align-items:center;padding-left:80px;z-index:2}
.nav a{color:var(--white);font-size:15px;font-weight:500;padding:8px 16px;margin-right:14px}
.nav a.active{background:rgba(255,255,255,.85);color:var(--green-dark)}
.hero-heading{left:327px;top:240px;color:var(--white);font-size:34px;font-weight:700;line-height:1.18;text-shadow:0 2px 6px rgba(0,0,0,.35)}
.hero-sub{left:327px;top:326px;color:var(--green);font-size:13px;line-height:1.35;font-weight:500}
.hero .btn{left:327px;top:372px;width:110px;height:30px;background:transparent;border:1px solid var(--white);font-size:10px}
.dots{display:flex;gap:8px}
.dots span{width:9px;height:9px;border-radius:50%;background:rgba(255,255,255,.5)}
.dots span.on{background:var(--white)}
.hero .dots{left:580px;top:472px}

/* services */
.services{top:515px;height:483px}
.services-intro{left:101px;top:49px;width:275px;height:289px;border:4px solid #d8d8d8;padding:38px 18px 0}
.services-intro h2{font-family:"PT Serif",Georgia,serif;font-size:21px;font-weight:400;color:var(--ink);line-height:1.15}
.services-intro h2 .green{font-weight:700}
.services-intro p{font-size:11px;line-height:1.55;margin-top:10px}
.services-intro .read-more{left:18px;bottom:14px}
.service-card{position:absolute;top:49px;width:228px}
.service-card .photo{position:relative;height:174px;width:228px}
.service-card h3{font-size:14px;font-weight:500;color:var(--ink);margin-top:34px}
.service-card p{font-size:10.5px;line-height:1.5;margin-top:10px}
.service-card .read-more{position:static;display:block;margin-top:14px}

/* galleries */
.galleries{top:998px;height:650px;background:var(--dark)}
.galleries .section-title{width:1200px;text-align:center;top:64px;color:var(--green);font-weight:500}
.galleries .intro{width:1200px;text-align:center;top:112px;font-size:12px;line-height:1.5;color:#a9a9a9}
.gallery-main{left:101px;top:173px;width:637px;height:339px;background:linear-gradient(135deg,#6f7a58,#4e5a3a 50%,#8a7a60)}
.gallery-grid{left:746px;top:173px;width:353px;height:339px;display:grid;grid-template-columns:repeat(3,1fr);grid-template-rows:repeat(3,1fr);gap:5px}
.gallery-grid span{display:block;background:linear-gradient(135deg,#6fa04e,#3f7a31)}
.gallery-grid span:nth-child(2n){background:linear-gradient(135deg,#7fae5c,#557f3a)}
.gallery-grid span:nth-child(3n){background:linear-gradient(135deg,#8e9c6e,#5c6c44)}
.galleries .btn{left:526px;top:573px;width:145px;height:34px;background:transparent;border:1px solid var(--green);color:var(--green);font-weight:500;font-size:11px}

/* about + estimate */
.about{top:1648px;height:535px}
.about .section-title{left:101px;top:95px;font-size:26px}
.about .underline{left:101px;top:133px;width:460px}
.about-text{left:101px;top:150px;width:460px;font-size:11.5px;line-height:1.6}
.about-text p+p{margin-top:12px}
.about .btn{left:101px;top:397px;width:135px;height:36px}
.estimate{left:607px;top:73px;width:492px;height:361px;border:4px solid #d8d8d8}
.estimate h2{position:absolute;left:92px;top:30px;font-size:24px;font-weight:500;color:var(--green)}
.estimate h2 .ink{color:var(--ink)}
.estimate .underline{left:92px;top:66px;width:310px}
.field{position:absolute;border:1px solid #cfcfcf;font-size:11px;color:var(--muted);padding:10px 12px;background:var(--white);white-space:nowrap;overflow:hidden}
.field.select::after{content:"";position:absolute;right:10px;top:16px;border:4px solid transparent;border-top-color:#777}
.estimate .btn{left:92px;top:294px;width:160px;height:32px;font-size:11px}

/* why */
.why{top:2183px;height:362px}
.why .section-title{left:101px;top:5px;font-size:26px;color:var(--green);font-weight:500}
.why .section-title .ink{color:var(--ink)}
.why .underline{left:101px;top:42px;width:640px}
.why-item{position:absolute;width:340px;height:98px;border:1px solid #ececec;padding:16px 18px 0 66px}
.why-icon{position:absolute;left:18px;top:14px;width:32px;height:32px}
.why-item h3{font-size:14px;font-weight:500;color:var(--ink)}
.why-item p{font-size:11px;line-height:1.5;margin-top:6px}

/* cta band */
.cta{top:2545px;height:304px;background:linear-gradient(90deg,#4f9f3f 0%,#6ec35a 50%,#3f8a36 100%)}
.cta .photo{inset:0}
.cta p{position:absolute;width:1200px;text-align:center;top:102px;font-size:21px;line-height:1.5;color:var(--white)}
.cta .btn{left:525px;top:196px;width:150px;height:40px}

/* news */
.news{top:2849px;height:593px}
.news .section-title{left:101px;top:64px;font-size:26px;color:var(--green);font-weight:500}
.news .section-title .ink{color:var(--ink);font-weight:700}
.news .underline{left:101px;top:101px;width:250px}
.news-card{position:absolute;top:138px;width:318px;height:440px;box-shadow:0 1px 6px rgba(0,0,0,.12);background:var(--white)}
.news-card .photo{position:relative;width:100%;height:209px}
.news-card h3{font-size:16px;font-weight:500;color:var(--ink);padding:26px 28px 0;line-height:1.3}
.news-card p{font-size:11px;line-height:1.55;padding:14px 28px 0}
.news-card .read-more{left:28px;bottom:36px}

/* testimonials */
.testimonials{top:3442px;height:572px;background:var(--light);clip-path:polygon(0 60px,50% 0,100% 60px,100% 100%,0 100%)}
.testimonials .section-title{width:1200px;text-align:center;top:160px;font-size:28px;color:var(--green);font-weight:500}
.testimonials .section-title .ink{color:var(--ink)}
.testimonials .underline{left:475px;top:200px;width:250px}
.avatar{position:absolute;width:40px;height:40px;border-radius:50%;background:linear-gradient(135deg,#c9b8a3,#8a7766)}
.person{position:absolute;font-size:11px;color:var(--ink);line-height:1.35}
.person small{display:block;font-size:10px;color:var(--muted)}
.quote{position:absolute;top:318px;width:376px;height:188px;background:var(--green);border-radius:12px;color:var(--white);font-size:12.5px;font-weight:500;line-height:1.55;padding:34px;text-align:center}
.quote::before{content:"";position:absolute;left:44px;top:-10px;border:10px solid transparent;border-bottom-color:var(--green);border-top:0}
.arrow{position:absolute;top:372px}
.testimonials .dots{left:585px;top:541px}
.testimonials .dots span{background:#cfcfcf;width:7px;height:7px}
.testimonials .dots span.on{background:var(--green)}

/* footer */
.footer{top:4014px;height:323px;background:var(--dark)}
.footer-brand{left:130px;top:60px;width:190px;display:flex;flex-direction:column;align-items:center;gap:10px}
.footer-brand .brand-dot{width:46px;height:46px}
.footer-brand .brand-name{font-size:22px;color:var(--white)}
.footer h4{position:absolute;font-size:17px;font-weight:700;color:var(--white)}
.footer-about{left:356px;top:100px;width:200px;font-size:11px;line-height:1.55;color:#bdbdbd}
.sitemap{left:680px;top:98px;font-size:11px;line-height:2;color:#cfcfcf;list-style:none}
.search{left:868px;top:60px;width:231px;height:30px;border:1px solid #777;font-size:11px;color:#aaa;padding:8px 10px}
.search::after{content:"";position:absolute;right:0;top:-1px;width:30px;height:30px;background:var(--green)}
.footer .socials{left:868px;top:126px;display:flex;gap:8px}
.footer .circle{width:25px;height:25px;border-color:#999}
.copyright{left:0;bottom:0;width:1200px;height:28px;background:var(--darker);text-align:center;font-size:11px;line-height:28px;color:#bdbdbd}
</style>
</head>
<body>

<header class="topbar">
  <span class="abs tagline">Providing Exceptional Landscaping</span>
  <div class="abs info"><span>Elmview &amp; Ridgefield County</span><span>410-555-0142</span><span>Mon-Sat: 07:00 - 17:00</span></div>
  <div class="abs socials"><span class="circle"></span><span class="circle"></span><span class="circle"></span></div>
</header>

<section class="hero">
  <span class="photo" role="img" aria-label="Landscaper in a cap and safety gear trimming a hedge in a sunlit garden"></span>
  <div class="abs brand-box"><span class="brand-dot"></span><span class="brand-name">Bright Furrow</span></div>
  <nav class="abs nav">
    <a class="active" href="#">Home</a><a href="#">About Us</a><a href="#">Services</a><a href="#">Galleries</a><a href="#">Blog</a><a href="#">Contact Us</a>
  </nav>
  <h1 class="abs hero-heading">The grass is always greener<br>On your side of the fence</h1>
  <p class="abs hero-sub">Lawns kept neat, fresh and green all season,<br>trimmed by hand with care.</p>
  <a class="btn" href="#">Learn More</a>
  <div class="abs dots"><span class="on"></span><span></span></div>
</section>

<section class="services">
  <div class="abs services-intro">
    <h2>Exceptional<br><span class="green">Services We Offer</span></h2>
    <p>We provide exceptional landscaping services to a wide range of commercial and residential properties for over 30 years, including large corporate environments, city parks, shopping malls and apartments. Our experienced landscapers set the standard each day in landscape design, paving, hardscaping. We will whip your yard into shape in no time.</p>
    <a class="read-more" href="#">See All Services &rsaquo;</a>
  </div>
  <article class="service-card" style="left:385px">
    <span class="photo" role="img" aria-label="Red lawn mower on a freshly striped green lawn" style="background:linear-gradient(160deg,#7cbf4f,#3f8a2c)"></span>
    <h3>Lawn Care and Mowing</h3>
    <p>We understand that your property is a big investment and we want our customers to know that we are there for them to help them accomplish the dreams that they may have for their property.</p>
    <a class="read-more" href="#">Read More &rsaquo;</a>
  </article>
  <article class="service-card" style="left:630px">
    <span class="photo" role="img" aria-label="Hedge trimmer shaping a dense green shrub" style="background:linear-gradient(160deg,#8fbf5a,#4d7f30)"></span>
    <h3>Shrub Trimming</h3>
    <p>We understand that your property is a big investment and we want our customers to know that we are there to help homeowners that they may have for their property.</p>
    <a class="read-more" href="#">Read More &rsaquo;</a>
  </article>
  <article class="service-card" style="left:873px">
    <span class="photo" role="img" aria-label="Worker in orange safety gear cutting a fallen tree" style="background:linear-gradient(160deg,#8a8f6c,#5a6d3c)"></span>
    <h3>Removal and Clean Up</h3>
    <p>While tree removal is the choice of last resort, it is sometimes most necessary. Sick trees, trees that uproot sidewalks, cause cracks in the foundation, disrupt power lines, have sustained.</p>
    <a class="read-more" href="#">Read More &rsaquo;</a>
  </article>
</section>

<section class="galleries">
  <h2 class="section-title">Project Galleries</h2>
  <p class="abs intro">With so many years of experience in the business, our company is your<br>source for the highest quality and landscaping service.</p>
  <span class="photo gallery-main" role="img" aria-label="Arborist with chainsaw and helmet cutting logs from a felled tree"></span>
  <div class="abs gallery-grid" role="img" aria-label="Grid of project photos: lawns, hedges, garden paths and a pavilion">
    <span></span><span></span><span></span><span></span><span></span><span></span><span></span><span></span><span></span>
  </div>
  <a class="btn" href="https://www.example-social.com/pg/BrightFurrowMD/photos/">Watch Gallery</a>
</section>

<section class="about">
  <h2 class="section-title"><span class="green">About</span> Our Company</h2>
  <div class="underline"></div>
  <div class="abs about-text">
    <p>Bright Furrow is a full-service landscaping company with a straightforward and unique design build philosophy. We believe in having one landscape designer handle the job from its conception on paper, to the realization on your property. The reason: by doing this you are able to communicate and work with a single individual, where you can share your thoughts and ideas with it to bring them, in collaboration, to life.</p>
    <p>Bright Furrow is made up of a group of highly skilled landscaping professionals who pay a lot of attention to small details. In the 30+ years of experience our staff keep your property looking and functioning beautifully. Our landscapers are fully licensed.</p>
  </div>
  <a class="btn" href="#">Learn More</a>

  <form class="abs estimate">
    <h2><span>Request</span> <span class="ink">An Estimate</span></h2>
    <div class="underline"></div>
    <div class="field" style="left:92px;top:97px;width:146px;height:38px">Your Name</div>
    <div class="field" style="left:251px;top:97px;width:151px;height:38px">Your Email</div>
    <div class="field select" style="left:92px;top:149px;width:146px;height:36px">Landscape Mainten</div>
    <div class="field" style="left:251px;top:149px;width:151px;height:36px">Your Phone</div>
    <div class="field" style="left:92px;top:194px;width:310px;height:84px">Your Message</div>
    <span class="btn">Request A Quote</span>
  </form>
</section>

<section class="why">
  <h2 class="section-title">Why <span class="ink">Choose Us</span></h2>
  <div class="underline"></div>

  <div class="why-item" style="left:101px;top:87px">
    <svg class="why-icon" viewBox="0 0 32 32"><path d="M6 24c0-12 8-18 20-18 0 12-6 20-18 20" fill="var(--green)"/><path d="M6 26l12-12" stroke="#fff" stroke-width="2"/></svg>
    <h3>Specialized Company</h3><p>We are a landscaping company specializing in residential and commercial landscaping.</p>
  </div>
  <div class="why-item" style="left:457px;top:87px">
    <svg class="why-icon" viewBox="0 0 32 32"><circle cx="16" cy="16" r="14" fill="var(--green)"/><path d="M9 16l5 5 9-10" stroke="#fff" stroke-width="3" fill="none"/></svg>
    <h3>Licensed &amp; Insured</h3><p>All our landscapers are fully licensed, bonded and insured.</p>
  </div>
  <div class="why-item" style="left:818px;top:87px">
    <svg class="why-icon" viewBox="0 0 32 32"><circle cx="16" cy="16" r="13" fill="none" stroke="var(--green)" stroke-width="4"/><circle cx="16" cy="16" r="5" fill="var(--green)"/></svg>
    <h3>Dependable Services</h3><p>We love to take pride in the work we do. Each project is finished in time and budget.</p>
  </div>
  <div class="why-item" style="left:101px;top:194px">
    <svg class="why-icon" viewBox="0 0 32 32"><rect x="4" y="7" width="24" height="21" rx="2" fill="none" stroke="var(--green)" stroke-width="3"/><path d="M4 13h24M10 4v6M22 4v6" stroke="var(--green)" stroke-width="3"/><path d="M11 20l4 3 6-6" stroke="var(--green)" stroke-width="2.5" fill="none"/></svg>
    <h3>Day Scheduling</h3><p>We schedule regular appointments to visit your property on the same day and time of the week.</p>
  </div>
  <div class="why-item" style="left:457px;top:194px">
    <svg class="why-icon" viewBox="0 0 32 32"><path d="M3 6h18v12H10l-5 4v-4H3z" fill="var(--green)"/><path d="M23 11h6v12h-2v4l-5-4h-9v-3h10z" fill="var(--green)"/></svg>
    <h3>Free Consultations</h3><p>We offer free consultations for our services, and will provide you with an actual quote.</p>
  </div>
  <div class="why-item" style="left:818px;top:194px">
    <svg class="why-icon" viewBox="0 0 32 32"><path d="M9 4h14v8a7 7 0 0 1-14 0z" fill="var(--green)"/><path d="M9 7H4c0 5 3 7 5 7M23 7h5c0 5-3 7-5 7" stroke="var(--green)" stroke-width="2.5" fill="none"/><rect x="14" y="18" width="4" height="6" fill="var(--green)"/><rect x="9" y="24" width="14" height="4" fill="var(--green)"/></svg>
    <h3>Reputable Company</h3><p>Operating for more than 30 years, earning a reputation for service and beautiful work.</p>
  </div>
</section>

<section class="cta">
  <span class="photo" role="img" aria-label="Close-up of a lawn mower on fresh grass, tinted green"></span>
  <p>Are you tired of spending hours mowing your lawn every weekend?<br>Take back your free time by having us take care of your garden</p>
  <a class="btn" href="#">Learn More</a>
</section>

<section class="news">
  <h2 class="section-title">Latest <span class="ink">news</span></h2>
  <div class="underline"></div>
  <article class="news-card" style="left:101px">
    <span class="photo" role="img" aria-label="Young gardener in a cap holding a tray of flowers" style="background:linear-gradient(160deg,#8cb366,#4e7d3b)"></span>
    <h3>Job: Fulltime (+50 hours per week) Landscapers</h3>
    <p>Lorem ipsum dolor sit amet, qui in esse munere mucius, cu lobortis definitiones eos, qui hinc integre splendide te. Augue ubique convenire has ex.</p>
    <a class="read-more" href="#">Read More &rsaquo;</a>
  </article>
  <article class="news-card" style="left:442px">
    <span class="photo" role="img" aria-label="Smiling gardener in a green apron among potted plants" style="background:linear-gradient(160deg,#7fa861,#3f6c35)"></span>
    <h3>We Won The 'Best Landscape Company' Award</h3>
    <p>Lorem ipsum dolor sit amet, qui in esse munere mucius, cu lobortis definitiones eos, qui hinc integre splendide te. Augue ubique convenire has ex.</p>
    <a class="read-more" href="#">Read More &rsaquo;</a>
  </article>
  <article class="news-card" style="left:784px">
    <span class="photo" role="img" aria-label="Couple choosing plants together at a garden center" style="background:linear-gradient(160deg,#c9bda8,#8fa67a)"></span>
    <h3>Why The Landscaper Is The Best For Business</h3>
    <p>Lorem ipsum dolor sit amet, qui in esse munere mucius, cu lobortis definitiones eos, qui hinc integre splendide te. Augue ubique convenire has ex.</p>
    <a class="read-more" href="#">Read More &rsaquo;</a>
  </article>
</section>

<section class="testimonials">
  <h2 class="section-title">Clients <span class="ink">Testimonials</span></h2>
  <div class="underline"></div>
  <span class="avatar" role="img" aria-label="Client portrait" style="left:318px;top:258px"></span>
  <p class="person" style="left:378px;top:260px">John Doe<small>CEO</small></p>
  <span class="avatar" role="img" aria-label="Client portrait" style="left:764px;top:258px"></span>
  <p class="person" style="left:824px;top:260px">John Doe<small>CEO</small></p>
  <blockquote class="quote" style="left:188px">I am slide content. Click edit button to change this text. Lorem ipsum dolor sit amet, consectetur adipiscing elit. Ut elit tellus, luctus nec ullamcorper mattis, pulvinar dapibus leo.</blockquote>
  <blockquote class="quote" style="left:636px">I am slide content. Click edit button to change this text. Lorem ipsum dolor sit amet, consectetur adipiscing elit. Ut elit tellus, luctus nec ullamcorper mattis, pulvinar dapibus leo.</blockquote>
  <svg class="arrow" style="left:104px" width="14" height="22" viewBox="0 0 14 22"><path d="M11 3L4 11l7 8" stroke="var(--green)" stroke-width="3" fill="none"/></svg>
  <svg class="arrow" style="left:1080px" width="14" height="22" viewBox="0 0 14 22"><path d="M3 3l7 8-7 8" stroke="var(--green)" stroke-width="3" fill="none"/></svg>
  <div class="abs dots"><span class="on"></span><span></span></div>
</section>

<footer class="footer">
  <div class="abs footer-brand"><span class="brand-dot"></span><span class="brand-name">Bright Furrow</span></div>
  <h4 style="left:356px;top:64px">About Us</h4>
  <p class="abs footer-about">I am text block. Click edit button to change this text. Lorem ipsum dolor sit amet, consectetur adipiscing elit. Ut elit tellus, luctus nec ullamcorper mattis, pulvinar dapibus leo.</p>
  <h4 style="left:680px;top:64px">Site Map</h4>
  <ul class="abs sitemap"><li>Home</li><li>About Us</li><li>Services</li><li>Galleries</li><li>Blog</li><li>Contact Us</li></ul>
  <div class="abs search">Search ...</div>
  <div class="abs socials"><a class="circle" href="https://social.example.com/brightfurrowmd" aria-label="Bright Furrow social page"></a><span class="circle"></span><span class="circle"></span><span class="circle"></span></div>
  <div class="abs copyright">&copy; 2018 Bright Furrow | All Rights Reserved.</div>
</footer>

</body>
</html>
```